Business Card Design

We need a business card with the contact information above listed on the front. On the rear we would like to list the services we provide. We are a full service beach home property management company. We provide Home Inspections, Building Projects, Kitchen and Bathroom Upgrades, Deck and Porch Construction, Plumbing-Electrical Repairs, Home Winterizing, Rental Damage Repairs, Winter Security Property Checks, Interior and Exterior Painting, Rental Maintenance Service Calls, Exterior Construction Upgrades.
We have been in business since 1998.

Reason: Need more time for approvals. President of the company on business trip and need a few more days. Thanks.

Reason: Need more time to figure out how this works. My designer I was working with stopped contacting me now I may have to start over.

Industry/Entity Type

Property Management

Contact Information for Business Card

Dorsey Works LLC.
48152 Red Maple Ct. Frankford DE 19871
Paul Dorsey President-Home Inspector Cell 302-555-0148 pdorsey@coralridgedesk.com
Kevin Dorsey Vice President Cell 302-555-0193 kdorsey@coralridgedesk.com
Office Fax 302-555-0127
Check us out on Facebook Dorsey Works LLC

Requirements
Must have
• We would like to have a logo designed, open to all suggestions. We are located in a beach community on the Atlantic Ocean in southern Delaware. We would like to convey somehow that they can leave their usually very expensive 2nd home to us and we will take care of everything. Would even entertain a slogan of some kind.

```html
<!DOCTYPE html>
<html lang="en">
<head>
<meta charset="utf-8">
<title>Dorsey Works LLC – Business Card</title>
<link href="https://fonts.googleapis.com/css2?family=Lato:wght@400;700;900&display=swap" rel="stylesheet">
<style>
  :root {
    --page: #eceae6;
    --paper: #f4f4f6;
    --navy: #2a4a6e;
    --navy-deep: #1f3a5c;
    --navy-light: #4a6a8c;
    --brand-blue: #1e3f8f;
    --skyline-a: #4d67b0;
    --skyline-b: #8fa0cf;
    --royal: #2f5fa8;
    --royal-deep: #1d4690;
    --green: #3fa045;
    --stripe-blue: #2a4fa0;
    --ink: #1c1c1c;
    --white: #ffffff;
  }
  * { box-sizing: border-box; margin: 0; padding: 0; }
  html, body {
    width: 1200px; height: 1000px; overflow: hidden;
    background: var(--page);
    font-family: "Lato", sans-serif;
  }
  .card {
    position: absolute; left: 290px; width: 620px; height: 350px;
    box-shadow: 0 8px 22px rgba(0,0,0,.25);
    overflow: hidden;
  }
  .skyline {
    position: absolute;
    background: linear-gradient(135deg, var(--skyline-a) 0%, var(--skyline-b) 100%);
  }
  .brand__name {
    position: absolute; color: var(--brand-blue); font-weight: 700;
    letter-spacing: 1px; white-space: nowrap;
  }

  /* Front */
  .card--front { top: 95px; background: var(--paper); }
  .card--front .skyline { left: 40px; top: 14px; width: 230px; height: 158px; }
  .card--front .brand__name { left: 28px; top: 70px; font-size: 34px; }
  .stripes { position: absolute; left: 0; right: 0; top: 172px; }
  .stripe { height: 5px; }
  .stripe--green { background: var(--green); }
  .stripe--blue { background: var(--stripe-blue); }
  .stripe--white { background: var(--white); height: 4px; }
  .front__band {
    position: absolute; left: 0; right: 0; top: 191px; bottom: 0;
    background: linear-gradient(180deg, var(--navy-light) 0%, var(--navy) 45%, var(--navy-deep) 100%);
  }
  .person { position: absolute; right: 26px; top: 118px; }
  .person__name {
    color: var(--brand-blue); font-weight: 700; font-size: 27px; letter-spacing: 1px;
    border-bottom: 2px solid var(--brand-blue); line-height: 1.15;
  }
  .person__title { color: var(--brand-blue); font-weight: 700; font-size: 14.5px; margin-top: 1px; }
  .contact { position: absolute; left: 22px; top: 206px; color: var(--white); font-size: 15px; list-style: none; }
  .contact li { display: flex; align-items: center; height: 23px; }
  .contact__icon { width: 20px; flex: none; display: flex; justify-content: center; }
  .contact__text { margin-left: 10px; }
  .contact li.contact--plain .contact__text { margin-left: 30px; }

  /* Back */
  .card--back {
    top: 510px;
    background: linear-gradient(180deg, var(--royal) 0%, var(--royal-deep) 100%);
  }
  .back__panel { position: absolute; inset: 26px 26px 30px 26px; background: var(--paper); }
  .card--back .skyline { left: 24px; top: 10px; width: 130px; height: 70px; }
  .card--back .brand__name { left: 18px; top: 40px; font-size: 22px; }
  .services { position: absolute; left: 22px; right: 18px; top: 92px; color: var(--ink); font-size: 13.5px; font-weight: 700; line-height: 1.45; }
  .services__intro { margin-bottom: 8px; }
</style>
</head>
<body>

<section class="card card--front" aria-label="Business card front">
  <div class="skyline" role="img" aria-label="Blue city skyline and road illustration"></div>
  <span class="brand__name">Dorsey Works LLC</span>
  <div class="person">
    <div class="person__name">PAUL DORSEY</div>
    <div class="person__title">President-Home Inspector</div>
  </div>
  <div class="stripes">
    <div class="stripe stripe--green"></div>
    <div class="stripe stripe--blue"></div>
    <div class="stripe stripe--white"></div>
    <div class="stripe stripe--green"></div>
  </div>
  <div class="front__band"></div>
  <ul class="contact">
    <li class="contact--plain"><span class="contact__text">48152 Red Maple Ct. Saltmeadow Bay 19871</span></li>
    <li><span class="contact__icon">
      <svg width="14" height="14" viewBox="0 0 14 14" aria-hidden="true"><rect x="3" y="1" width="8" height="4" fill="none" stroke="#fff" stroke-width="1.3"/><rect x="1" y="5" width="12" height="6" rx="1" fill="#fff"/><rect x="3.5" y="9" width="7" height="4" fill="#fff" stroke="#2a4a6e" stroke-width="1"/></svg>
    </span><span class="contact__text">302-555-0127</span></li>
    <li><span class="contact__icon">
      <svg width="10" height="15" viewBox="0 0 10 15" aria-hidden="true"><rect x="0.7" y="0.7" width="8.6" height="13.6" rx="1.5" fill="none" stroke="#fff" stroke-width="1.3"/><circle cx="5" cy="12" r="0.9" fill="#fff"/></svg>
    </span><span class="contact__text">302-555-0148</span></li>
    <li><span class="contact__icon">
      <svg width="15" height="11" viewBox="0 0 15 11" aria-hidden="true"><rect x="0.7" y="0.7" width="13.6" height="9.6" fill="none" stroke="#fff" stroke-width="1.3"/><path d="M1 1 L7.5 6 L14 1" fill="none" stroke="#fff" stroke-width="1.3"/></svg>
    </span><span class="contact__text">pdorsey@coralridgedesk.com</span></li>
    <li><span class="contact__icon">
      <svg width="14" height="14" viewBox="0 0 14 14" aria-hidden="true"><circle cx="7" cy="7" r="7" fill="#3b5d9c"/></svg>
    </span><span class="contact__text">shorepage.net/Dorsey Works LLC</span></li>
  </ul>
</section>

<section class="card card--back" aria-label="Business card back">
  <div class="back__panel">
    <div class="skyline" role="img" aria-label="Blue city skyline and road illustration"></div>
    <span class="brand__name">Dorsey Works LLC</span>
    <div class="services">
      <p class="services__intro">We are a full service beach home property management company<br>We provide&nbsp;&nbsp;:</p>
      <p>Home Inspections, Building Projects, Kitchen and Bathroom Upgrades, Deck and Porch Construction, Plumbing-Electrical Repairs, Home Winterizing, Rental Damage Repairs, Winter Security Property Checks, Interior and Exterior Painting, Rental Maintenance Service Calls, Exterior Construction Upgrades.</p>
    </div>
  </div>
</section>

</body>
</html>
```